Amber Ridge Publishing Web Page Design

Design a website for my new start up publishing company - Amber Ridge Publishing, the first work published by ARP with be a new book by M.R. Theodor called Silent Ledger. The prototype for the book cover is attached.

Target Market(s)

Worldwide, all readers of mystery, fiction, etc.

Industry/Entity Type

Book Publisher

Coding

Coded - Design and coding required

Number of Pages Required

1 page

```html
<!DOCTYPE html>
<html lang="en">
<head>
<meta charset="utf-8">
<title>Amber Ridge Publishing</title>
<link href="https://fonts.googleapis.com/css2?family=Lato:wght@400;700;900&display=swap" rel="stylesheet">
<style>
:root{
  --blue:#1b75bb;
  --orange:#f9a100;
  --yellow:#ffd200;
  --ink:#333333;
  --text:#444444;
  --muted:#e6e6e6;
  --panel:#f3f3f3;
  --hero:#1f1b17;
  --white:#ffffff;
}
*{margin:0;padding:0;box-sizing:border-box}
html,body{width:1200px;height:2526px;overflow:hidden;background:var(--white)}
body{font-family:'Lato',sans-serif;color:var(--text);position:relative}
.abs{position:absolute}
.logo{font-weight:700;font-size:36px;color:#555;letter-spacing:.3px}
.nav{top:45px;right:52px;display:flex;gap:33px;font-size:15px;color:var(--ink)}
.nav .active{color:var(--blue);font-weight:700}
.hero{top:107px;left:0;width:1200px;height:445px;background:linear-gradient(90deg,#2a241d 0%,#1c1915 55%,#2b2620 100%)}
.hero-title{left:75px;top:208px;font-size:58px;font-weight:900;color:var(--yellow);letter-spacing:.5px}
.hero-sub{left:75px;top:278px;width:520px;font-size:24px;line-height:34px;color:var(--white)}
.btn{display:block;width:141px;height:43px;background:var(--orange);color:var(--white);font-size:20px;font-weight:700;text-align:center;line-height:43px}
.cover{background:linear-gradient(160deg,#1d2b6e 0%,#2a3c97 45%,#11184a 100%);border-right:14px solid #d9d9d9;box-shadow:4px 6px 14px rgba(0,0,0,.35)}
.photo{background:linear-gradient(135deg,#5a3425 0%,#3b2218 55%,#2a1912 100%)}
.h2{font-size:28px;font-weight:700;color:var(--blue)}
.para{font-size:15px;line-height:26px;color:var(--text)}
.side-word{font-size:62px;font-weight:900;color:var(--muted);letter-spacing:1px;white-space:nowrap}
.panel{left:0;width:1200px;background:var(--panel)}
.review h3{font-size:25px;color:var(--blue);font-weight:700}
.stars{margin-top:6px;display:flex;gap:3px}
.review p{margin-top:12px;font-size:15px;line-height:24px;width:300px}
.person{margin-top:28px;display:flex;align-items:center;gap:21px}
.avatar{width:89px;height:86px;background:linear-gradient(180deg,#c9c3bd,#7d766f)}
.person b{display:block;font-size:20px;color:var(--blue)}
.person span{font-size:17px;color:var(--ink)}
.blog-img{background:linear-gradient(135deg,#3a3129 0%,#241f1a 60%,#191613 100%)}
.date{font-size:15px;font-weight:700;color:var(--ink);display:flex;align-items:center;gap:18px}
.foot-h{font-size:20px;font-weight:700;color:var(--blue)}
.foot-list{font-size:15px;line-height:29px;color:var(--ink);list-style:none}
.social{display:flex;gap:20px}
.social span{width:20px;height:20px;border-radius:50%;background:var(--ink);display:block}
.subscribe{display:flex;width:242px;height:41px;border:1px solid #ccc}
.subscribe .field{flex:1;font-size:13px;color:#555;padding:12px 10px}
.subscribe .go{width:46px;background:var(--orange);color:var(--white);font-weight:700;font-size:16px;text-align:center;line-height:39px}
</style>
</head>
<body>

<header>
  <div class="abs logo" style="left:75px;top:32px">Amber Ridge</div>
  <nav class="abs nav">
    <span class="active">Home</span><span>About Author</span><span>About Book</span><span>Services</span><span>Reviews</span><span>Blog</span><span>Contact Us</span>
  </nav>
</header>

<section class="abs hero" role="img" aria-label="Dark desk background with an old book and reading glasses"></section>
<h1 class="abs hero-title">SILENT LEDGER</h1>
<p class="abs hero-sub">Praesent tempus vel nibh id ullamcorperdonec rutrum leo non ipsum vehicula&nbsp; convallis vel enim maximus..</p>
<a class="abs btn" style="left:75px;top:395px">Read More</a>
<div class="abs cover" style="left:752px;top:145px;width:276px;height:440px;transform:rotate(3deg)" role="img" aria-label="Silent Ledger book cover by M.R. Theodor"></div>

<section>
  <div class="abs photo" style="left:75px;top:614px;width:421px;height:365px" role="img" aria-label="Author writing at a typewriter in a study"></div>
  <h2 class="abs h2" style="left:524px;top:670px">About M.R. Theodor</h2>
  <p class="abs para" style="left:524px;top:712px;width:520px">Vestibulum accumsan tellus ac ante sollicitudin facilisis nec sit amet ex. Maecenas euismod bibendum metus sit amet varius. Aenean ut dui sapien. Donec gravida metus et venenatis efficitur. Curabitur sed urna odio. Pellentesque in metus massa. Maecenas at sem urna. Fusce viverra erat elit, elementum consequat nisl dictum sagittis.</p>
  <a class="abs btn" style="left:524px;top:868px">Read More</a>
  <div class="abs side-word" style="left:1080px;top:620px;transform-origin:0 0;transform:rotate(90deg) translateY(-62px);left:1140px">ABOUT ME</div>
</section>

<section class="abs panel" style="top:1040px;height:428px"></section>
<div class="abs side-word" style="left:58px;top:1352px;transform-origin:0 0;transform:rotate(-90deg)">BOOK</div>
<h2 class="abs h2" style="left:164px;top:1126px">About Silent Ledger</h2>
<p class="abs para" style="left:164px;top:1168px;width:525px">Vestibulum accumsan tellus ac ante sollicitudin facilisis nec sit amet ex. Maecenas euismod bibendum metus sit amet varius. Aenean ut dui sapien. Donec gravida metus et venenatis efficitur. Curabitur sed urna odio. Pellentesque in metus massa. Maecenas at sem urna. Fusce viverra erat elit, elementum consequat nisl dictum sagittis.</p>
<a class="abs btn" style="left:164px;top:1324px">Read More</a>
<div class="abs cover" style="left:752px;top:1057px;width:276px;height:440px;transform:rotate(3deg)" role="img" aria-label="Silent Ledger book cover by M.R. Theodor"></div>

<section>
  <div class="abs review" style="left:75px;top:1514px">
    <h3>Donec gravida</h3>
    <div class="stars"><svg width="88" height="14" viewBox="0 0 88 14"><g fill="#f9a100"><path id="st" d="M7 0l1.7 4.6H13l-3.6 2.8 1.4 4.6L7 9.2 3.2 12l1.4-4.6L1 4.6h4.3z"/><use href="#st" x="18"/><use href="#st" x="36"/><use href="#st" x="54"/><use href="#st" x="72"/></g></svg></div>
    <p>Vestibulum accumsan tellus ac ante sollicitudin facilisis nec sit amet eaecenas euismod bibendum metus sit amet varius ut dui sapien gravida metus..</p>
    <div class="person"><div class="avatar" role="img" aria-label="Reviewer portrait"></div><div><b>Name Heading</b><span>Location</span></div></div>
  </div>
  <div class="abs review" style="left:434px;top:1514px">
    <h3>Donec gravida</h3>
    <div class="stars"><svg width="88" height="14" viewBox="0 0 88 14"><g fill="#f9a100"><use href="#st"/><use href="#st" x="18"/><use href="#st" x="36"/><use href="#st" x="54"/><use href="#st" x="72"/></g></svg></div>
    <p>Vestibulum accumsan tellus ac ante sollicitudin facilisis nec sit amet eaecenas euismod bibendum metus sit amet varius ut dui sapien gravida metus..</p>
    <div class="person"><div class="avatar" role="img" aria-label="Reviewer portrait"></div><div><b>Name Heading</b><span>Location</span></div></div>
  </div>
  <div class="abs review" style="left:795px;top:1514px">
    <h3>Donec gravida</h3>
    <div class="stars"><svg width="88" height="14" viewBox="0 0 88 14"><g fill="#f9a100"><use href="#st"/><use href="#st" x="18"/><use href="#st" x="36"/><use href="#st" x="54"/><use href="#st" x="72"/></g></svg></div>
    <p>Vestibulum accumsan tellus ac ante sollicitudin facilisis nec sit amet eaecenas euismod bibendum metus sit amet varius ut dui sapien gravida metus..</p>
    <div class="person"><div class="avatar" role="img" aria-label="Reviewer portrait"></div><div><b>Name Heading</b><span>Location</span></div></div>
  </div>
  <div class="abs side-word" style="left:1140px;top:1502px;transform-origin:0 0;transform:rotate(90deg) translateY(-62px);left:1140px">REVIEWS</div>
</section>

<section class="abs panel" style="top:1845px;height:401px"></section>
<div class="abs side-word" style="left:58px;top:2135px;transform-origin:0 0;transform:rotate(-90deg)">BLOG</div>
<div class="abs blog-img" style="left:136px;top:1897px;width:451px;height:293px" role="img" aria-label="Evidence board with pinned notes in a dim room"></div>
<h2 class="abs h2" style="left:613px;top:1894px;width:520px;line-height:34px">Donec gravida metus et venenatis efficitur aptent taciti.</h2>
<div class="abs date" style="left:613px;top:1970px">
  <svg width="15" height="15" viewBox="0 0 15 15"><rect x="1" y="3" width="13" height="11" fill="none" stroke="#f9a100" stroke-width="1.5"/><rect x="1" y="3" width="13" height="3" fill="#f9a100"/><rect x="4" y="1" width="1.5" height="3" fill="#f9a100"/><rect x="9.5" y="1" width="1.5" height="3" fill="#f9a100"/></svg>
  July, 10, 2019
</div>
<p class="abs para" style="left:613px;top:2000px;width:530px">Vestibulum accumsan tellus ac ante sollicitudin facilisis nec sit amet ex. Maecenas euismod bibendum metus sit amet varius. Aenean ut dui sapien. Donec gravida metus et venenatis efficitur. Curabitur sed urna odio. Pellentesque in metus massa. Maecenas at sem urna. Fusce viverra erat elit, elementum consequat nisl dictum sagittis.</p>
<a class="abs btn" style="left:613px;top:2148px">Read More</a>

<footer>
  <div class="abs logo" style="left:75px;top:2290px">Amber Ridge</div>
  <p class="abs" style="left:75px;top:2354px;font-size:13px;line-height:22px;color:var(--ink)">Copyright© 2019 Company Name<br>All Right Reserved</p>
  <div class="abs social" style="left:75px;top:2414px" aria-label="Social links"><span></span><span></span><span></span><span></span><span></span></div>

  <div class="abs foot-h" style="left:342px;top:2292px">Quick Links</div>
  <ul class="abs foot-list" style="left:342px;top:2323px"><li>Home</li><li>About Author</li><li>About Book</li><li>Services</li></ul>
  <ul class="abs foot-list" style="left:485px;top:2323px"><li>Reviews</li><li>Blog</li><li>Contact Us</li></ul>

  <div class="abs foot-h" style="left:639px;top:2292px">Resources</div>
  <ul class="abs foot-list" style="left:639px;top:2323px"><li>Sed finibus posuere</li><li>Auguea cursus</li><li>Duis ultricies metus</li><li>Posuere condimentum</li></ul>

  <div class="abs foot-h" style="left:884px;top:2292px">Email Subscribe</div>
  <p class="abs" style="left:884px;top:2323px;font-size:15px;line-height:29px;color:var(--ink)">Sed finibus posuere auguea cursus</p>
  <div class="abs subscribe" style="left:884px;top:2361px"><div class="field">Email Address</div><div class="go">GO</div></div>
</footer>

</body>
</html>
```